Webdesign für Metallbau-Wasserkraft Tessmar Lauber GmbH & Co. KG
Zielgruppe
Das Unternehmen ist im Metall- und Stahlwasserbau tätig. Die Haupkompetenz liegt im Stahlwasserbau, Rechenreinigung und Stahlbau tätig.
Aufgabenstellung
Die vorhandenen Seite https://www.metallbau-tessmar-lauber-beispiel.de/ soll einen Relaunch erhalten. Das Design soll frisch, modern und aussagekräftig erscheinen, trotz der Tradition und des Handwerksbetriebes.
Die Navigationstruktur soll erhalten bleiben. Hinzu kommt der Punkt 'Neuigkeiten'.

```html
<!DOCTYPE html>
<html lang="de">
<head>
<meta charset="utf-8">
<title>Metallbau-Wasserkraft Tessmar Lauber GmbH &amp; Co. KG</title>
<link href="https://fonts.googleapis.com/css2?family=Figtree:wght@400;500;600;700&display=swap" rel="stylesheet">
<style>
:root{
  --blue:#0a6cb4;
  --blue-dark:#075a98;
  --ink:#1b1b1b;
  --text:#4a4a4a;
  --muted:#6b6b6b;
  --card:#f8f8f8;
  --band:#f7f7f7;
  --white:#ffffff;
}
*{margin:0;padding:0;box-sizing:border-box}
html,body{width:1200px;height:2425px;overflow:hidden;background:var(--white)}
body{position:relative;font-family:"Figtree",sans-serif;color:var(--text)}
.abs{position:absolute}
a{color:inherit;text-decoration:none}

/* header */
.brand{left:163px;top:42px;width:210px;height:43px;border-top:2px solid var(--blue);border-bottom:2px solid var(--blue);display:flex;align-items:center;gap:8px}
.brand-mark{width:26px;height:26px;background:var(--blue);flex:none}
.brand-name{font-weight:700;font-size:11px;line-height:12px;color:var(--blue);text-transform:uppercase}
.nav{left:579px;top:54px;display:flex;gap:24px;font-size:12px;color:var(--ink);align-items:center;height:18px}
.nav-cta{left:938px;top:48px;width:99px;height:30px;background:var(--blue);color:var(--white);border-radius:6px;font-size:12px;display:flex;align-items:center;justify-content:center}

/* hero */
.hero{left:163px;top:121px;width:874px;height:425px;border-radius:20px;overflow:hidden;background:linear-gradient(180deg,#5f7a4a 0%,#8a9a7e 25%,#c9d3d6 45%,#7fa3bd 70%,#1b74b8 100%)}
.tags{left:18px;top:15px;display:flex;gap:10px}
.tag{background:var(--white);color:var(--blue);font-size:10px;border-radius:12px;padding:4px 11px}
.hero-title{left:0;width:874px;top:256px;text-align:center;color:var(--white);font-weight:700;font-size:38px;line-height:51px}
.hero-sub{left:0;width:874px;top:359px;text-align:center;color:var(--white);font-size:11px}

/* sections */
.h1{font-weight:600;font-size:26px;color:var(--ink)}
.h2{font-weight:600;font-size:22px;color:var(--ink)}
.lead{font-size:11.5px;line-height:20px;color:var(--text)}

.service{top:837px;width:245px;height:183px;background:var(--card);border-radius:8px;padding:19px 14px}
.service h3{font-size:16px;font-weight:600;color:var(--blue);margin-bottom:8px}
.service p{font-size:11.5px;line-height:20px}
.btn{position:absolute;left:14px;top:139px;width:132px;height:30px;background:var(--blue);color:var(--white);font-size:11.5px;border-radius:5px;display:flex;align-items:center;justify-content:center}

.project{left:163px;top:1148px;width:874px;height:425px;border-radius:20px;overflow:hidden;background:linear-gradient(180deg,#0b6db3 0%,#2d7fbe 14%,#3f6b3a 30%,#c9ccc6 45%,#b7bfb4 62%,#3a4a4f 80%,#8c7f6e 100%)}
.project-title{left:35px;top:28px;color:var(--white);font-weight:700;font-size:21px}
.project-sub{left:35px;top:62px;color:var(--white);font-size:11.5px}
.slider-ctrl{left:779px;top:391px;width:82px;height:23px;background:var(--white);border-radius:6px;display:flex;align-items:center;justify-content:center;gap:5px}
.dot{width:4px;height:4px;border-radius:50%;background:#c8d6e3}
.dot.on{background:var(--blue)}

/* news */
.band{left:0;top:1642px;width:1200px;height:783px;background:var(--band)}
.news{top:1809px;width:279px;min-height:301px;background:var(--white);border-radius:6px;overflow:hidden}
.news-img{height:164px;background:linear-gradient(180deg,#7d8a95 0%,#9aa39a 40%,#6e7570 65%,#4d5358 100%)}
.news-body{padding:14px 18px 18px}
.news h3{font-size:12.5px;line-height:20px;font-weight:600;color:var(--blue);margin-bottom:5px}
.news p{font-size:11px;line-height:20px;letter-spacing:-0.1px}
.news .more{display:inline-block;margin-top:4px;font-size:11px;line-height:16px;font-weight:600;color:var(--ink);text-decoration:underline}

/* footer */
.foot-brand{left:128px;top:2233px}
.foot-note{left:128px;top:2289px;width:260px;font-size:10px;line-height:17.5px;color:var(--muted)}
.badge{top:2350px;height:23px;background:#d9dfe8}
.foot-col{top:2241px;font-size:10px;color:var(--muted)}
.foot-col h4{font-size:11.5px;font-weight:600;color:var(--blue);margin-bottom:9px}
.foot-col li{list-style:none;line-height:20px}
</style>
</head>
<body>

<header>
  <a class="abs brand" href="#"><span class="brand-mark"></span><span class="brand-name">Metallbau-Wasserkraft<br>Tessmar Lauber<br>GmbH &amp; Co. KG</span></a>
  <nav class="abs nav"><a href="#">Start</a><a href="#">Über uns</a><a href="#">Unser Angebot ▾</a><a href="#">Partner</a><a href="#">Aktuelles</a></nav>
  <a class="abs nav-cta" href="#">Jetzt Anfragen</a>
</header>

<section class="abs hero" role="img" aria-label="Foto eines Wehrs mit Wasserkraftanlage am Fluss">
  <div class="abs tags"><span class="tag">Stahlwasserbau</span><span class="tag">Rechenreiniger</span><span class="tag">Stahlbau</span></div>
  <h1 class="abs hero-title">Stahlwasserbau mit<br>Tradition und Innovation</h1>
  <p class="abs hero-sub">Ihr Partner für Metallbau und Stahlwasserbau in Auenstein bei Lindenfurt</p>
</section>

<h2 class="abs h1" style="left:163px;top:604px">Metallbau Wasserkraft Tessmar Lauber</h2>
<p class="abs lead" style="left:163px;top:646px;width:760px">Metallbau Wasserkraft Tessmar Lauber – ein Name, der in ganz Deutschland für qualitativ hochwertigen Stahlwasser- und Metallbau, fachgerechte Montage und umfassenden Kundenservice steht. Als erfahrener Fachbetrieb in Auenstein bei Lindenfurt fertigen und montieren wir verschiedenste Produkte aus den Bereichen Stahlbau, Geländebau nach GEL-Vorschriften sowie Tor- und Treppenanlagen</p>

<h2 class="abs h2" style="left:163px;top:763px">Unsere Produkte und Dienstleistungen</h2>
<p class="abs lead" style="left:163px;top:798px">Folgende Produkte können wir als versierter Fachbetrieb für Sie fertigen:</p>

<article class="abs service" style="left:163px"><h3>Stahlwasserbau</h3><p>Schützanlagen, Dammtafeln, Wehrklappen, Fischaufstiegshilfen, Rechenanlagen, Schwimmbalken, Hochwasserschutztore</p><a class="btn" href="#">Mehr Informationen</a></article>
<article class="abs service" style="left:439px"><h3>Stahlwasserbau</h3><p>Stangenreiniger, Horizontal-<br>Rechenreiniger, Knickarmreiniger</p><a class="btn" href="#">Mehr Informationen</a></article>
<article class="abs service" style="left:715px"><h3>Stahlwasserbau</h3><p>Treppen &amp; Stege, Geländer</p><a class="btn" href="#">Mehr Informationen</a></article>

<h2 class="abs h2" style="left:163px;top:1077px">Bisherige Projekte</h2>
<p class="abs lead" style="left:163px;top:1112px">Folgende Produkte können wir als versierter Fachbetrieb für Sie fertigen:</p>

<section class="abs project" role="img" aria-label="Foto einer Schützanlage mit Treppe und Geländer an einem Fluss">
  <h3 class="abs project-title">Schützanlagen</h3>
  <p class="abs project-sub">Kompetenter Stahlwasserbau aus Auenstein</p>
  <div class="abs slider-ctrl">
    <svg width="10" height="12" viewBox="0 0 10 12"><path d="M7 1 2 6l5 5" fill="none" stroke="#0a6cb4" stroke-width="1.6"/></svg>
    <span class="dot on"></span><span class="dot"></span><span class="dot"></span><span class="dot"></span>
    <svg width="10" height="12" viewBox="0 0 10 12"><path d="M3 1l5 5-5 5" fill="none" stroke="#0a6cb4" stroke-width="1.6"/></svg>
  </div>
</section>

<div class="abs band"></div>
<h2 class="abs h2" style="left:163px;top:1706px">Aktuelle Nachrichten</h2>
<p class="abs lead" style="left:163px;top:1741px;width:570px">Lorem ipsum dolor sit amet, consetetur sadipscing elitr, sed diam nonumy eirmod tempor invidunt ut labore et dolore magna aliquyam erat, sed diam voluptua. At vero eos et accusam et justo duo dolores et ea rebum.</p>

<article class="abs news" style="left:163px"><div class="news-img" role="img" aria-label="Foto einer Rechenreinigungsanlage am Fluss vor Wohnhäusern"></div><div class="news-body"><h3>Schützanlagen zur Regelung des Wasserflusses fertiggstellt</h3><p>Lorem ipsum dolor sit amet, consetetur<br>sadipscing elitr, sed diam nonumy eirmo tempor</p><a class="more" href="#">Mehr lesen</a></div></article>
<article class="abs news" style="left:457px"><div class="news-img" role="img" aria-label="Foto einer Rechenreinigungsanlage am Fluss vor Wohnhäusern"></div><div class="news-body"><h3>Schützanlagen zur Regelung des Wasserflusses fertiggstellt</h3><p>Lorem ipsum dolor sit amet, consetetur<br>sadipscing elitr, sed diam nonumy eirmo tempor</p><a class="more" href="#">Mehr lesen</a></div></article>
<article class="abs news" style="left:751px"><div class="news-img" role="img" aria-label="Foto einer Rechenreinigungsanlage am Fluss vor Wohnhäusern"></div><div class="news-body"><h3>Schützanlagen zur Regelung des Wasserflusses fertiggstellt</h3><p>Lorem ipsum dolor sit amet, consetetur<br>sadipscing elitr, sed diam nonumy eirmo tempor</p><a class="more" href="#">Mehr lesen</a></div></article>

<footer>
  <a class="abs brand foot-brand" href="#"><span class="brand-mark"></span><span class="brand-name">Metallbau-Wasserkraft<br>Tessmar Lauber<br>GmbH &amp; Co. KG</span></a>
  <p class="abs foot-note">Gefördert wurde dieses Vorhaben durch das E-Business-Programm aus der Mittelstandsrichtlinie der Landesförderbank.</p>
  <div class="abs badge" style="left:128px;width:30px"></div>
  <div class="abs badge" style="left:168px;width:58px"></div>
  <div class="abs foot-col" style="left:562px"><h4>Linksammlung</h4><ul><li>Startseite</li><li>Über uns</li><li>Unser Angebot</li><li>Partner</li><li>Aktuelles</li><li>Sitemap</li></ul></div>
  <div class="abs foot-col" style="left:723px"><h4>Rechtliches</h4><ul><li>Impressum</li><li>Datenschutz</li><li>AGB</li><li>Cookie-Richtlinien</li></ul></div>
  <div class="abs foot-col" style="left:890px"><h4>Kontaktiere uns</h4><ul><li>Telefon: 03741 55 20 48</li><li>Telefax: 03741 55 20 47</li><li>E-Mail: info@metallbau-tessmar-lauber-beispiel.de</li></ul></div>
</footer>

</body>
</html>
```